I have a logo and need to design the business card and stationery.

The uploaded logo image named as FERNHOLT CONSTRUCTION which is to be replaced to FERNHOLT CONTRACTS. Kindly add below details and submit the designs- Company name- Fernholt Engineering Contracts LLP Name & Post- Varun Kelkar (Designated Partner) Address- Block No.712, Wing C, Tulsa Trade Court, Moti Lal Road, Pawar Industrial Estate, Goregaon(E), Mumbai - 400 063 Contact- +91 97410 58263 Email- varunkelkar@mailnest.example Website- www.fernholtcontracts.example Contact for Letterhead- +91-22-27481195

Hi Tanvir Haque, We are liking your Design #41927306. We have suggested some changes which are mentioned in feedback. Kindly revert with it asap to finalize this design.

Colors

Designer to choose colors to be used in the design.

```html
<!DOCTYPE html>
<html lang="en">
<head>
<meta charset="utf-8">
<title>Fernholt Contracts – Business Card</title>
<link rel="stylesheet" href="https://fonts.googleapis.com/css2?family=Urbanist:wght@400;600;700&display=swap">
<style>
  :root {
    --ink: #121212;
    --paper: #f1f1f1;
    --stage: #d9d7d5;
    --muted: #cfcfcf;
    --band-text: #1b1b1b;
  }
  * { margin: 0; padding: 0; box-sizing: border-box; }
  html, body { width: 1200px; height: 1014px; overflow: hidden; }
  body {
    background: var(--stage);
    font-family: "Urbanist", sans-serif;
    position: relative;
  }
  .card {
    position: absolute;
    left: 203px;
    width: 794px;
    height: 440px;
    background: var(--ink);
    overflow: hidden;
  }
  .card--back { top: 52px; }
  .card--front { top: 522px; }

  /* back side */
  .back-brand {
    position: absolute;
    top: 110px; left: 0; right: 0;
    display: flex; flex-direction: column; align-items: center; gap: 18px;
  }
  .brand-square { width: 46px; height: 46px; background: var(--paper); }
  .brand-name {
    color: var(--paper);
    font-weight: 700;
    font-size: 26px;
    letter-spacing: 4px;
  }
  .address-band {
    position: absolute;
    top: 341px; left: 0; right: 0; height: 40px;
    background: var(--paper);
    display: flex; align-items: center; justify-content: center;
    text-align: center;
    color: var(--band-text);
    font-size: 16.5px;
    line-height: 1.15;
  }

  /* front side */
  .front-panel {
    position: absolute;
    top: 0; left: 0; bottom: 0; width: 366px;
    background: var(--paper);
    display: flex; flex-direction: column; align-items: center; justify-content: center; gap: 22px;
  }
  .front-panel .brand-square { width: 90px; height: 90px; background: var(--ink); }
  .front-panel .brand-name { color: var(--ink); font-size: 30px; letter-spacing: 3px; }

  .front-info { position: absolute; left: 384px; top: 72px; color: var(--paper); }
  .company-name {
    font-weight: 700;
    font-size: 25px;
    letter-spacing: 1.5px;
    line-height: 1.1;
  }
  .person { margin-top: 82px; }
  .person-name { font-size: 29px; font-weight: 400; }
  .person-name b { font-weight: 700; }
  .person-title { font-size: 17px; color: var(--muted); margin-top: 2px; }

  .contacts { list-style: none; margin-top: 56px; }
  .contacts li {
    display: flex; align-items: center; gap: 9px;
    font-size: 18px; color: var(--muted);
    height: 27px;
  }
  .contacts svg { width: 16px; height: 16px; flex: none; }
</style>
</head>
<body>

<section class="card card--back">
  <div class="back-brand">
    <span class="brand-square"></span>
    <span class="brand-name">FERNHOLT CONTRACTS</span>
  </div>
  <div class="address-band">
    <p>Block No.712, Wing C, Tulsa Trade Court, Moti Lal Road,<br>Pawar Industrial Estate, Goregaon(E), Mumbai - 400 063</p>
  </div>
</section>

<section class="card card--front">
  <div class="front-panel">
    <span class="brand-square"></span>
    <span class="brand-name">FERNHOLT</span>
  </div>
  <div class="front-info">
    <p class="company-name">FERNHOLT CONTRACTS</p>
    <div class="person">
      <p class="person-name"><b>Varun</b> Kelkar</p>
      <p class="person-title">(Designated Partner)</p>
    </div>
    <ul class="contacts">
      <li>
        <svg viewBox="0 0 16 16" aria-hidden="true"><circle cx="8" cy="8" r="8" fill="#cfcfcf"/><path d="M5.2 4.2l1.4-.3.8 1.9-.9.7c.5 1 1.2 1.8 2.2 2.3l.7-.9 1.9.8-.3 1.4c-3.3.1-5.9-2.6-5.8-5.9z" fill="#121212"/></svg>
        +91 97410 58263
      </li>
      <li>
        <svg viewBox="0 0 16 16" aria-hidden="true"><circle cx="8" cy="8" r="8" fill="#cfcfcf"/><rect x="4" y="5.2" width="8" height="5.6" fill="#121212"/><path d="M4 5.4L8 8.4l4-3" stroke="#cfcfcf" stroke-width=".9" fill="none"/></svg>
        varunkelkar@mailnest.example
      </li>
      <li>
        <svg viewBox="0 0 16 16" aria-hidden="true"><circle cx="8" cy="8" r="8" fill="#cfcfcf"/><g stroke="#121212" stroke-width=".9" fill="none"><circle cx="8" cy="8" r="4.4"/><ellipse cx="8" cy="8" rx="1.9" ry="4.4"/><path d="M3.6 8h8.8M4.3 5.8h7.4M4.3 10.2h7.4"/></g></svg>
        www.fernholtcontracts.example
      </li>
    </ul>
  </div>
</section>

</body>
</html>
```